Anzeigengestaltung für Teppichwäscherei
Zielgruppe
Wir sind eine Teppichwäscherei mit sitz in Recklinghausen.
Wir waschen alle arten von Teppichen vorallem hochwertige perser und designer teppiche.
Zu unserem service gehört auch die Teppichreparatur und restauration von alten und antiken stücken.
unsere zielgruppe sind private haushalte ab 40+ die auch ein teppich zuhause haben.
Aufgabenstellung
es soll modern kreative und auffällig sein aber nicht so das ältere kunden abgeschreckt sind.
folgende sachen müssen drin sein - Teppichreinigung & Teppichreparatur - Kostenlose (gratis ) Abholung und lieferung -
Format: 2sp./100mm & 3sp./100mm & 4sp./225mm
-Normalwäsche statt 19€ jetzt 16 €
-Vollwäsche statt 27€ jetzt 24 €
-Seidenwäsche statt 49€ jetzt 40 €
angebot gilt nur 5 Tage
vom xx.xx.xx bis zum xx.xx.xx

```html
<!DOCTYPE html>
<html lang="de">
<head>
<meta charset="utf-8">
<title>Fadenglanz Teppichpflege – Anzeige</title>
<link rel="stylesheet" href="https://fonts.googleapis.com/css2?family=Fira+Sans:wght@400;500;700;800&display=swap">
<style>
  :root{
    --brand-blue:#1f3a8a;
    --text-grey:#555555;
    --white:#ffffff;
  }
  html,body{margin:0;padding:0;overflow:hidden;background:var(--white);}
  .ad{position:relative;width:1200px;height:1200px;overflow:hidden;background:var(--white);font-family:"Fira Sans",sans-serif;}
  .ad-shapes{position:absolute;inset:0;}
  .brand-name{position:absolute;left:85px;top:196px;width:280px;text-align:center;font-weight:700;font-size:38px;letter-spacing:1.5px;color:var(--brand-blue);line-height:44px;}
  .headline{position:absolute;left:62px;top:424px;margin:0;font-weight:800;font-size:47.5px;line-height:54.5px;color:var(--brand-blue);letter-spacing:-0.2px;}
  .offer-list{position:absolute;left:63px;top:672px;margin:0;padding:0;list-style:none;font-size:31.5px;color:var(--text-grey);}
  .offer-list li{height:54.3px;line-height:44px;}
  .contact-address{position:absolute;left:66px;top:1020px;font-size:27px;line-height:36px;color:var(--white);font-style:normal;}
  .contact-lines{position:absolute;left:408px;top:1008px;font-size:26px;color:var(--white);}
  .contact-line{display:flex;align-items:center;height:44px;}
  .contact-icon{width:34px;height:34px;margin-right:14px;flex:none;}
  .website{position:absolute;left:270px;top:1150px;font-size:26px;color:var(--brand-blue);}
</style>
</head>
<body>
<div class="ad">
  <svg class="ad-shapes" width="1200" height="1200" viewBox="0 0 1200 1200">
    <defs>
      <linearGradient id="rugPhoto" x1="0.2" y1="0" x2="0.8" y2="1">
        <stop offset="0" stop-color="#9c3b33"/>
        <stop offset="0.3" stop-color="#8a7874"/>
        <stop offset="0.45" stop-color="#c9c3bf"/>
        <stop offset="0.6" stop-color="#c2463a"/>
        <stop offset="0.8" stop-color="#5e2a24"/>
        <stop offset="1" stop-color="#b8392f"/>
      </linearGradient>
      <linearGradient id="rugSmall" x1="0" y1="0" x2="1" y2="1">
        <stop offset="0" stop-color="#c9c4be"/>
        <stop offset="0.45" stop-color="#b8392f"/>
        <stop offset="1" stop-color="#8a2a24"/>
      </linearGradient>
    </defs>
    <path class="band-top" d="M22 22 H1200 V420 L650 330 C470 210 230 150 22 195 Z" fill="var(--brand-blue)"/>
    <circle class="brand-disc" cx="225" cy="218" r="162" fill="var(--white)"/>
    <circle class="brand-ring" cx="225" cy="218" r="142" fill="none" stroke="var(--brand-blue)" stroke-width="3"/>
    <rect class="band-bottom" x="22" y="978" width="1000" height="155" fill="var(--brand-blue)"/>
    <circle cx="1292" cy="620" r="626" fill="var(--white)"/>
    <circle cx="1292" cy="620" r="612" fill="url(#rugPhoto)" role="img" aria-label="Foto: Reinigungsmaschine schäumt einen roten Orientteppich ein"/>
    <circle cx="700" cy="408" r="130" fill="var(--white)"/>
    <circle cx="700" cy="408" r="117" fill="url(#rugSmall)" role="img" aria-label="Foto: roter Teppich wird mit Wasserstrahl gespült"/>
  </svg>

  <div class="brand-name">FADENGLANZ</div>

  <h1 class="headline">Teppichreinigung &amp;<br>Teppichreparatur -<br>Kostenlose (gratis )<br>Abholung und lieferung</h1>

  <ul class="offer-list">
    <li>Normalwäsche statt 19€ jetzt 16 €</li>
    <li>Vollwäsche statt 27€ jetzt 24 €</li>
    <li>Seidenwäsche statt 49€ jetzt 40 €</li>
    <li>angebot gilt nur 5 Tage</li>
    <li>vom xx.xx.xx bis zum xx.xx.xx</li>
  </ul>

  <address class="contact-address">Lindenhofstraße 12<br>45659 Recklinghausen</address>

  <div class="contact-lines">
    <div class="contact-line">
      <svg class="contact-icon" viewBox="0 0 34 34" aria-hidden="true">
        <circle cx="17" cy="17" r="17" fill="var(--white)"/>
        <path d="M11 9.5c1-.8 2-.6 2.6.3l1.6 2.6c.5.8.3 1.6-.4 2.1l-1 .8c.8 1.8 2.1 3.2 3.9 4.1l.9-1c.6-.7 1.4-.8 2.2-.3l2.6 1.6c.9.6 1 1.6.2 2.6-1.3 1.6-3 1.9-4.9 1-3.4-1.6-6.2-4.4-7.8-7.9-.8-1.8-.5-3.6 1.1-4.9z" fill="var(--brand-blue)"/>
      </svg>
      <span>02361 / 58 204 36</span>
    </div>
    <div class="contact-line">
      <svg class="contact-icon" viewBox="0 0 34 34" aria-hidden="true">
        <circle cx="17" cy="17" r="17" fill="var(--white)"/>
        <rect x="9" y="11" width="16" height="12" rx="1.5" fill="none" stroke="var(--brand-blue)" stroke-width="1.8"/>
        <path d="M9.5 12 L17 18 L24.5 12" fill="none" stroke="var(--brand-blue)" stroke-width="1.8"/>
      </svg>
      <span>kontakt@fadenglanz-pflege.de</span>
    </div>
  </div>

  <div class="website">www.fadenglanz-pflege.de</div>
</div>
</body>
</html>
```